design cheese package for BRUVO

We want someone to give me some graphic designs for the cheese package. You shall not only design it on the basis of our product sizes, but also the design with my company Logo shall be novel and attactive. There are some pictures in the attachments: picture 1--3 for my product; picture 4 for my company Logo; picture 5--6 for your reference Thanks! please add the word BRUVO in the package design, thanks!

Industry/Entity Type

Product

```html
<!DOCTYPE html>
<html lang="en">
<head>
<meta charset="utf-8">
<title>BRUVO Sharp Cheddar – Package Label</title>
<link rel="stylesheet" href="https://fonts.googleapis.com/css2?family=Lobster&family=Questrial&family=Stardos+Stencil:wght@700&display=swap">
<style>
  :root {
    --paper: #ffffff;
    --green-dark: #1f3d1f;
    --green: #4a7a3a;
    --outline: #3a6633;
    --sky: #e6ddd0;
    --field-light: #cfc2ae;
    --field-dark: #8f7d66;
    --wood: #ddd7cd;
    --wood-line: #c4bcae;
    --back-tan: #c9b39b;
    --ink: #2a2a2a;
    --cheese-light: #ece3c8;
    --cheese-dark: #d8c79a;
  }
  html, body {
    margin: 0;
    width: 1200px;
    height: 1132px;
    overflow: hidden;
    background: var(--paper);
  }
  .canvas { display: block; width: 1200px; height: 1132px; }
  .title-sharp { font-family: "Lobster", cursive; font-size: 86px; fill: var(--green-dark); stroke: var(--paper); stroke-width: 6px; paint-order: stroke; }
  .title-cheddar { font-family: "Lobster", cursive; font-size: 64px; fill: var(--green); stroke: var(--paper); stroke-width: 5px; paint-order: stroke; }
  .subtitle { font-family: "Questrial", sans-serif; font-size: 32px; letter-spacing: 3px; fill: var(--ink); }
  .brand-name { font-family: "Questrial", sans-serif; fill: var(--green-dark); }
  .ingredients-title { font-family: "Stardos Stencil", sans-serif; font-weight: 700; font-size: 20px; letter-spacing: 1px; fill: var(--ink); }
  .facts-heading { font-family: "Questrial", sans-serif; font-size: 13px; letter-spacing: 2px; fill: var(--ink); }
  .facts-row { font-family: "Questrial", sans-serif; font-size: 9.5px; fill: var(--ink); }
  .facts-bold { font-family: "Questrial", sans-serif; font-size: 9.5px; font-weight: 700; fill: var(--ink); }
  .facts-other { font-family: "Questrial", sans-serif; font-size: 11px; fill: var(--ink); }
  .die-outline { fill: none; stroke: var(--outline); stroke-width: 5; }
</style>
</head>
<body>
<svg class="canvas" viewBox="0 0 1200 1132" xmlns="http://www.w3.org/2000/svg">
  <defs>
    <linearGradient id="field-tone" x1="0" y1="0" x2="0" y2="1">
      <stop offset="0" stop-color="var(--sky)"/>
      <stop offset="0.35" stop-color="var(--field-dark)"/>
      <stop offset="1" stop-color="var(--field-light)"/>
    </linearGradient>
    <linearGradient id="cheese-tone" x1="0" y1="0" x2="1" y2="1">
      <stop offset="0" stop-color="var(--cheese-light)"/>
      <stop offset="1" stop-color="var(--cheese-dark)"/>
    </linearGradient>
    <clipPath id="face-clip"><circle cx="296" cy="311" r="243"/></clipPath>
    <clipPath id="die-clip">
      <path d="M236,546.5 A243,243 0 1 1 356,546.5 L356,748 A170,170 0 1 1 236,748 Z"/>
    </clipPath>

    <g id="label-face">
      <rect x="40" y="60" width="520" height="520" fill="var(--sky)"/>
      <rect class="pasture-photo" x="40" y="170" width="520" height="200" fill="url(#field-tone)" role="img" aria-label="Sepia photo of cows grazing in a pasture"/>
      <rect class="wood-planks" x="40" y="360" width="520" height="220" fill="var(--wood)" role="img" aria-label="Weathered white wooden planks"/>
      <rect class="cheese-photo" x="200" y="365" width="280" height="165" fill="url(#cheese-tone)" role="img" aria-label="Photo of a wedge of aged cheddar with crumbled pieces"/>
      <circle cx="258" cy="125" r="9" fill="var(--green)"/>
      <text class="brand-name" x="274" y="133" font-size="22">BRUVO</text>
      <text class="title-sharp" x="292" y="308" transform="rotate(-4 400 280)">Sharp</text>
      <text class="title-cheddar" x="104" y="360" transform="rotate(-4 220 340)">Cheddar</text>
      <text class="subtitle" x="113" y="408">natural</text>
      <text class="subtitle" x="113" y="438">cheese</text>
    </g>
  </defs>

  <g class="die-label">
    <g clip-path="url(#die-clip)">
      <rect class="wood-planks" x="230" y="540" width="132" height="230" fill="var(--wood)" role="img" aria-label="Weathered white wooden planks"/>
      <line x1="262" y1="540" x2="262" y2="770" stroke="var(--wood-line)"/>
      <line x1="318" y1="540" x2="318" y2="770" stroke="var(--wood-line)"/>
      <circle cx="296" cy="907" r="170" fill="var(--back-tan)"/>
      <g clip-path="url(#face-clip)"><use href="#label-face"/></g>

      <g class="ingredients-panel" transform="rotate(180 296 907)">
        <text class="ingredients-title" x="296" y="770" text-anchor="middle">INGREDIENTS</text>
        <rect x="180" y="784" width="206" height="235" fill="none" stroke="var(--ink)" stroke-width="1.5"/>
        <text class="facts-heading" x="186" y="800">Supplement Facts</text>
        <text class="facts-row" x="186" y="814">Serving Size: 1 Packet (6.65g)</text>
        <rect x="180" y="819" width="206" height="4" fill="var(--ink)"/>
        <text class="facts-bold" x="186" y="834">Amount per Packet</text>
        <text class="facts-bold" x="380" y="834" text-anchor="end">% DV</text>
        <line x1="180" y1="838" x2="386" y2="838" stroke="var(--ink)"/>
        <text class="facts-row" x="186" y="850">Vitamin E</text><text class="facts-row" x="290" y="850">350mg</text><text class="facts-row" x="380" y="850" text-anchor="end">2333 %</text>
        <text class="facts-row" x="186" y="863">Vitamin C</text><text class="facts-row" x="290" y="863">60mg</text><text class="facts-row" x="380" y="863" text-anchor="end">67 %</text>
        <line x1="180" y1="867" x2="386" y2="867" stroke="var(--ink)"/>
        <text class="facts-bold" x="186" y="879">Proprietary Blend</text><text class="facts-bold" x="290" y="879">2940mg</text>
        <text class="facts-row" x="190" y="892">NAC - Essential Amino Acid</text><text class="facts-row" x="380" y="892" text-anchor="end">*</text>
        <text class="facts-row" x="190" y="905">Dandelion Root Extract</text><text class="facts-row" x="380" y="905" text-anchor="end">*</text>
        <text class="facts-row" x="190" y="918">Gypsywood Extract</text><text class="facts-row" x="380" y="918" text-anchor="end">*</text>
        <text class="facts-row" x="190" y="931">L-Glutamine</text><text class="facts-row" x="380" y="931" text-anchor="end">*</text>
        <text class="facts-row" x="190" y="944">St. Mary Thistle Extract</text><text class="facts-row" x="380" y="944" text-anchor="end">*</text>
        <text class="facts-row" x="190" y="957">Asparagus Root Extract</text><text class="facts-row" x="380" y="957" text-anchor="end">*</text>
        <text class="facts-row" x="190" y="970">Prickly Pear Extract</text><text class="facts-row" x="380" y="970" text-anchor="end">*</text>
        <text class="facts-row" x="190" y="983">European Elder Flower Extract</text><text class="facts-row" x="380" y="983" text-anchor="end">*</text>
        <text class="facts-row" x="190" y="996">Lady's Mantel Extract</text><text class="facts-row" x="380" y="996" text-anchor="end">*</text>
        <rect x="180" y="1000" width="206" height="3" fill="var(--ink)"/>
        <text class="facts-row" x="186" y="1014">*Daily Value (DV) not established.</text>
        <text class="facts-other" x="296" y="1036" text-anchor="middle">Other Ingredients: Honey Powder</text>
      </g>
    </g>
    <path class="die-outline" d="M236,546.5 A243,243 0 1 1 356,546.5 L356,748 A170,170 0 1 1 236,748 Z"/>
  </g>

  <g class="brand-mark">
    <circle cx="900" cy="170" r="22" fill="var(--green-dark)"/>
    <text class="brand-name" x="938" y="192" font-size="60">BRUVO</text>
  </g>

  <g class="lid-face" transform="translate(564 459)">
    <g clip-path="url(#face-clip)"><use href="#label-face"/></g>
    <circle cx="296" cy="311" r="243" class="die-outline"/>
  </g>
</svg>
</body>
</html>
```